Vintage Style Soup Package Label

I make dry soup packages. I am looking for a label for my soups that shows Quality, Homemade Goodness. Easy, Delicious. My company is called Uncle Barnaby Pantry, But I want this soup line to be called "Thistle & Rye " All my product has a very Vintage Antique look.
I Love Typography. My 6 cup soups are packaged in a flat black bag.
my website is www.unclebarnabypantry.example. I have 15 different Flavours. Our motto is Simple Suppers, Every Day.
While creating the label if you wanted to use
Please use "Chicken Pot Pie" as your sample please and thanks.

Target Market(s)

I want to sell my soups to upscale Grocery and Specialty stores.

Font styles to use
Serif
Sans Serif
Other font styles liked:
• Castellar

Colors
6c449b
ec1f27
ffc214
9ccb3b
ffffff
f37122

Requirements
Must have
• NOTE: A place for weight needs to be on the label

My labels I print on are Vertical 3.33 x4"
Colours. I do not like Pink or Pastel colours. I prefer Dark or grunge colours.
Nice to have
• NOTE: I live in Canada so my packaging is supposed to have English and French on it. The rule state because I am a small business I do not have to. But if you can figure a way to put in the design that would be fine but not necessary. If you did add it to the design it does not have to be the same size font as the English.
Should not have
• Pastel Colours.

```html
<!DOCTYPE html>
<html lang="en">
<head>
<meta charset="utf-8">
<title>Uncle Barnaby Pantry – Thistle &amp; Rye Chicken Pot Pie Label</title>
<link rel="stylesheet" href="https://fonts.googleapis.com/css2?family=Cinzel:wght@400&family=Rye&family=Alegreya+SC:wght@500&family=Josefin+Sans:wght@600&display=swap">
<style>
  :root {
    --stage: #000000;
    --frame-brown: #8a6a3e;
    --frame-dark: #5a4326;
    --panel-edge: #0d2527;
    --panel-teal: #1d4d53;
    --panel-teal-deep: #163e43;
    --ink-light: #e6e6e4;
    --ink-gold: #cdb47a;
    --badge-red: #a3141d;
    --ribbon: #d3d3d1;
    --ribbon-ink: #2a2a2a;
  }
  * { box-sizing: border-box; margin: 0; padding: 0; }
  html, body {
    width: 1200px; height: 612px; overflow: hidden;
    background: var(--stage);
  }
  .label {
    position: absolute; left: 367px; top: 26px;
    width: 466px; height: 560px;
    background: linear-gradient(135deg, var(--frame-brown), var(--frame-dark) 55%, var(--frame-brown));
  }
  .label__panel {
    position: absolute; inset: 18px;
    border: 5px solid var(--panel-edge);
    background: radial-gradient(ellipse at 50% 40%, var(--panel-teal), var(--panel-teal-deep));
  }
  .abs { position: absolute; }
  .center { left: 0; right: 0; text-align: center; }

  .brand-ornament {
    left: 118px; top: 56px; width: 232px; height: 42px;
    border-radius: 20px; background: rgba(205,180,122,0.14);
  }
  .brand-name {
    top: 67px; font-family: "Josefin Sans", sans-serif; font-weight: 600;
    font-size: 15px; letter-spacing: 1.6px; color: var(--ink-gold);
  }
  .badge {
    left: 368px; top: 35px; width: 72px; height: 72px;
    border-radius: 50%; background: var(--badge-red);
  }

  .title-main {
    top: 122px; font-family: "Cinzel", serif; font-weight: 400; font-size: 66px;
    line-height: 1; color: var(--ink-light); letter-spacing: 1px;
  }
  .title-sub {
    top: 190px; font-family: "Cinzel", serif; font-weight: 400; font-size: 48px;
    line-height: 1; color: var(--ink-light);
  }
  .leaf {
    top: 197px; width: 40px; height: 40px; border-radius: 6px;
    background: var(--ink-light); opacity: 0.85;
  }
  .leaf--left { left: 70px; }
  .leaf--right { left: 356px; }

  .rule { left: 92px; width: 282px; height: 3px; background: var(--ink-light); border-radius: 2px; }
  .rule--top { top: 272px; transform: rotate(1deg); }
  .rule--bottom { top: 336px; transform: rotate(1deg); }
  .flourish {
    top: 272px; width: 30px; height: 84px; border-radius: 16px;
    background: rgba(230,230,228,0.3);
  }
  .flourish--left { left: 40px; }
  .flourish--right { left: 396px; }
  .line-name {
    top: 290px; font-family: "Rye", serif; font-size: 30px;
    line-height: 1; color: var(--ink-light); transform: rotate(2deg);
  }

  .ready {
    top: 356px; font-family: "Alegreya SC", serif; font-weight: 500;
    font-size: 27px; line-height: 44px; color: var(--ink-gold); letter-spacing: 0.3px;
  }
  .ready__num { font-size: 40px; }

  .ribbon {
    left: 56px; top: 420px; width: 354px; height: 64px;
    border-radius: 10px; background: var(--ribbon);
    transform: rotate(4deg);
  }
  .motto {
    top: 440px; font-family: "Alegreya SC", serif; font-weight: 500;
    font-size: 21px; line-height: 1.2; color: var(--ribbon-ink); transform: rotate(4deg);
  }
  .weight {
    top: 497px; font-family: "Alegreya SC", serif; font-weight: 500;
    font-size: 28px; line-height: 1.1; color: var(--ink-gold);
  }
</style>
</head>
<body>
  <main class="label">
    <div class="label__panel" role="img" aria-label="Teal panel with a faint woven chevron pattern"></div>

    <div class="abs brand-ornament" role="img" aria-label="Gold filigree scrollwork framing the brand name"></div>
    <p class="abs center brand-name">UNCLE BARNABY PANTRY</p>
    <div class="abs badge" role="img" aria-label="Round origin seal"></div>

    <h1 class="abs center title-main">CHICKEN</h1>
    <div class="abs leaf leaf--left" role="img" aria-label="Maple leaf ornament"></div>
    <h2 class="abs center title-sub">POT PIE</h2>
    <div class="abs leaf leaf--right" role="img" aria-label="Maple leaf ornament"></div>

    <div class="abs rule rule--top"></div>
    <div class="abs flourish flourish--left" role="img" aria-label="Hand-drawn swirl flourish"></div>
    <p class="abs center line-name">THISTLE &amp; RYE</p>
    <div class="abs flourish flourish--right" role="img" aria-label="Hand-drawn swirl flourish"></div>
    <div class="abs rule rule--bottom"></div>

    <p class="abs center ready">Ready in <span class="ready__num">3</span> Minutes</p>

    <div class="abs ribbon" role="img" aria-label="Engraved curling ribbon banner"></div>
    <p class="abs center motto">Simple Suppers, Every Day</p>

    <p class="abs center weight">30G</p>
  </main>
</body>
</html>
```